Wealth Education Business Needs Sharp Business Card Design

We need a business card design for a recently launched investor education business called Harbor Ledger.

The final design should promote security, empowerment, self improvement and financial gain. The card will ideally promote the stature of the business.

For more information and colours please visit harborledger-example.com.au

Target Market(s)

Corporate executives and high net worth individuals

Industry/Entity Type

Education

Contact Information for Business Card

Name
Position
Contact Address
Phone
Mobile
Email
Website

```html
<!DOCTYPE html>
<html lang="en">
<head>
<meta charset="utf-8">
<title>Harbor Ledger – Business Card</title>
<link rel="stylesheet" href="https://fonts.googleapis.com/css2?family=Lato:wght@400;700&display=swap">
<style>
  :root {
    --backdrop: #3b3b3c;
    --card: #fdfdfd;
    --ink: #333335;
    --accent-teal: #168a86;
    --name-band: #5b5c5e;
    --contact-band: #232f45;
    --light-text: #ffffff;
  }
  * { margin: 0; padding: 0; box-sizing: border-box; }
  html, body {
    width: 1200px;
    height: 960px;
    overflow: hidden;
    background: var(--backdrop);
    font-family: "Lato", Arial, sans-serif;
  }
  .canvas {
    position: relative;
    width: 1200px;
    height: 960px;
  }
  .card {
    position: absolute;
    left: 270px;
    width: 645px;
    height: 369px;
    background: var(--card);
    box-shadow: 0 3px 10px rgba(0,0,0,0.35);
    overflow: hidden;
  }
  .card--front { top: 83px; }
  .card--back  { top: 507px; }

  .wordmark {
    position: absolute;
    display: flex;
    align-items: center;
    gap: 18px;
    color: var(--ink);
    font-weight: 400;
    text-transform: uppercase;
    letter-spacing: 0.18em;
    white-space: nowrap;
  }
  .wordmark__dot {
    width: 16px;
    height: 16px;
    border-radius: 50%;
    background: var(--accent-teal);
    flex: none;
  }
  .card--front .wordmark {
    left: 50%;
    top: 163px;
    transform: translateX(-50%);
    font-size: 38px;
  }
  .card--back .wordmark {
    right: 44px;
    top: 86px;
    font-size: 33px;
  }

  .name-band {
    position: absolute;
    left: 0;
    top: 226px;
    width: 100%;
    height: 35px;
    background: var(--name-band);
    color: var(--light-text);
    display: flex;
    align-items: center;
    padding-left: 37px;
  }
  .name-band__name { font-weight: 700; font-size: 18px; }
  .name-band__role { font-size: 15px; margin-left: 6px; }

  .contact-band {
    position: absolute;
    left: 0;
    top: 268px;
    width: 100%;
    height: 101px;
    background: var(--contact-band);
    color: var(--light-text);
    font-size: 14px;
  }
  .contact-group {
    position: absolute;
    top: 28px;
    line-height: 22px;
    white-space: nowrap;
  }
  .contact-group--phones { left: 31px; }
  .contact-group--web { left: 166px; }
  .contact-group--address { left: 458px; }
  .contact-line {
    display: flex;
    align-items: center;
    gap: 8px;
  }
  .contact-line svg { width: 15px; height: 15px; flex: none; }
  .divider {
    position: absolute;
    top: 26px;
    width: 1.5px;
    height: 50px;
    background: var(--light-text);
  }
  .divider--first { left: 152px; }
  .divider--second { left: 444px; }
</style>
</head>
<body>
<main class="canvas">

  <section class="card card--front" aria-label="Card front">
    <div class="wordmark"><span>Harbor Ledger</span><span class="wordmark__dot"></span></div>
  </section>

  <section class="card card--back" aria-label="Card back">
    <div class="wordmark"><span>Harbor Ledger</span><span class="wordmark__dot"></span></div>

    <div class="name-band">
      <span class="name-band__name">Daniel Whitford -</span>
      <span class="name-band__role">Founder &amp; CEO</span>
    </div>

    <div class="contact-band">
      <div class="contact-group contact-group--phones">
        <div class="contact-line">
          <svg viewBox="0 0 16 16" aria-hidden="true"><path fill="#fff" d="M2 5c0-2 3-3 6-3s6 1 6 3v1h-3V4.8C10 4.4 9 4.2 8 4.2S6 4.4 5 4.8V6H2zM4 7h8l2 6H2z"/></svg>
          <span>1300.555.014</span>
        </div>
        <div class="contact-line">
          <svg viewBox="0 0 16 16" aria-hidden="true"><rect x="4" y="1" width="8" height="14" rx="1.5" fill="none" stroke="#fff" stroke-width="1.5"/><circle cx="8" cy="12.5" r="0.9" fill="#fff"/></svg>
          <span>0000.000.000</span>
        </div>
      </div>
      <span class="divider divider--first"></span>
      <div class="contact-group contact-group--web">
        <div class="contact-line">
          <svg viewBox="0 0 16 16" aria-hidden="true"><rect x="1" y="3" width="14" height="10" fill="#fff"/><path d="M1.5 3.5 8 9l6.5-5.5" fill="none" stroke="#232f45" stroke-width="1.3"/></svg>
          <span>info@harborledger-example.com.au</span>
        </div>
        <div class="contact-line">
          <svg viewBox="0 0 16 16" aria-hidden="true"><g fill="none" stroke="#fff" stroke-width="1.3"><circle cx="8" cy="8" r="6.5"/><ellipse cx="8" cy="8" rx="3" ry="6.5"/><path d="M1.5 8h13M2.5 4.8h11M2.5 11.2h11"/></g></svg>
          <span>www.harborledger-example.com.au</span>
        </div>
      </div>
      <span class="divider divider--second"></span>
      <div class="contact-group contact-group--address">
        <div>Level 2, 47 Quayside Row</div>
        <div>Melbourne VIC 3000</div>
      </div>
    </div>
  </section>

</main>
</body>
</html>
```